New LGBT Nightclub Crowdfunding Poster

We need it to read well for social media posts. All colors should look similar to Seattle’s Sports Teams color schemes.

The top should have: The logo prominently with the fans in the background photo. and then still center and important, "Coming soon!" "You can be part of the first in line for the amazing things happening". (The call to action is the purchase of these amazing deals for the first weekend open / passes. That should be clear).

```html
<!DOCTYPE html>
<html lang="en">
<head>
<meta charset="UTF-8">
<title>The Encore – Coming Soon Poster</title>
<link rel="stylesheet" href="https://fonts.googleapis.com/css2?family=Exo+2:ital,wght@1,900&family=Teko:wght@400;600&family=Open+Sans:ital,wght@0,400;0,700;1,400;1,700&family=Russo+One&display=swap">
<style>
  :root {
    --canvas: #e9eaec;
    --navy: #0b1f47;
    --navy-deep: #071634;
    --green: #6cc24a;
    --lime: #9ccf3c;
    --violet: #6f68cf;
    --sky: #8fb8f0;
    --mint: #d9f3c6;
    --white: #ffffff;
    --text-soft: #d7deea;
  }
  * { box-sizing: border-box; margin: 0; padding: 0; }
  html, body { width: 1200px; height: 1200px; overflow: hidden; background: var(--canvas); }
  .poster {
    position: absolute; left: 221px; top: 30px; width: 758px; height: 1140px;
    background:
      radial-gradient(ellipse 60% 35% at 50% 58%, rgba(255,255,255,0.7), transparent 70%),
      linear-gradient(180deg, var(--violet) 0%, var(--sky) 22%, var(--mint) 45%, var(--green) 66%, var(--green) 100%);
    overflow: hidden;
    font-family: "Open Sans", sans-serif;
  }
  .light-rays { position: absolute; inset: 0; width: 100%; height: 700px; }
  .logo {
    position: absolute; left: 50%; top: 40px; transform: translateX(-50%);
    width: 240px; height: 240px; border-radius: 50%;
    background: radial-gradient(circle, #2a3d78 0%, #1b2c5e 55%, rgba(27,44,94,0) 72%);
    display: flex; align-items: center; justify-content: center;
  }
  .logo-name {
    font-family: "Teko", sans-serif; font-weight: 600; font-size: 46px; line-height: 0.95;
    color: var(--white); text-align: center; letter-spacing: 1px;
  }
  .headline {
    position: absolute; top: 335px; left: 0; width: 100%; text-align: center;
    font-family: "Exo 2", sans-serif; font-style: italic; font-weight: 900;
    font-size: 82px; letter-spacing: 2px; color: var(--navy);
    text-shadow: 3px 3px 0 rgba(255,255,255,0.55);
  }
  .tagline {
    position: absolute; top: 478px; left: 0; width: 100%; text-align: center;
    font-family: "Teko", sans-serif; font-weight: 600; font-size: 44px; color: var(--navy); line-height: 1;
  }
  .subline {
    position: absolute; top: 530px; left: 0; width: 100%; text-align: center;
    font-family: "Teko", sans-serif; font-weight: 400; font-size: 33px; color: var(--navy); line-height: 1;
  }
  .crowd {
    position: absolute; left: 0; top: 640px; width: 100%; height: 120px;
    background: linear-gradient(180deg, rgba(11,31,71,0) 0%, rgba(11,31,71,0.6) 45%, var(--navy) 100%);
  }
  .funding-panel {
    position: absolute; left: 0; top: 760px; width: 100%; height: 380px; background: var(--navy);
  }
  .levels-box {
    position: absolute; left: 27px; top: 65px; width: 703px; height: 255px;
    border: 2px dotted var(--lime); border-radius: 12px;
  }
  .levels-title {
    position: absolute; top: -14px; left: 50%; transform: translateX(-50%);
    background: var(--navy); padding: 0 16px;
    font-family: "Russo One", sans-serif; font-size: 20px; color: var(--white); letter-spacing: 1px; white-space: nowrap;
  }
  .levels-col { position: absolute; top: 28px; list-style: none; }
  .levels-col.left { left: 18px; width: 320px; }
  .levels-col.right { left: 372px; width: 316px; }
  .divider { position: absolute; left: 344px; top: 32px; width: 1px; height: 190px; background: linear-gradient(180deg, transparent, var(--text-soft), transparent); }
  .level {
    position: relative; padding-left: 22px; margin-bottom: 12px;
    font-size: 11.5px; line-height: 1.38; color: var(--text-soft);
  }
  .level::before { content: "»"; position: absolute; left: 2px; top: -3px; color: var(--lime); font-size: 16px; font-weight: 700; }
  .level em { font-weight: 700; font-style: italic; color: var(--white); }
  .note { margin-top: 26px; padding-left: 22px; font-size: 10.5px; font-style: italic; color: var(--white); }
  .site {
    position: absolute; top: 342px; left: 0; width: 100%; text-align: center;
    font-family: "Exo 2", sans-serif; font-style: italic; font-weight: 900; font-size: 16px;
    letter-spacing: 2px; color: var(--lime);
  }
</style>
</head>
<body>
<main class="poster">
  <svg class="light-rays" viewBox="0 0 758 700" aria-hidden="true">
    <defs>
      <linearGradient id="ray" x1="0" y1="0" x2="0" y2="1">
        <stop offset="0" stop-color="#ffffff" stop-opacity="0.55"/>
        <stop offset="1" stop-color="#ffffff" stop-opacity="0"/>
      </linearGradient>
    </defs>
    <polygon points="20,0 70,0 330,640 250,640" fill="url(#ray)"/>
    <polygon points="738,0 688,0 428,640 508,640" fill="url(#ray)"/>
    <polygon points="0,40 0,100 300,700 220,700" fill="url(#ray)" opacity="0.5"/>
    <polygon points="758,40 758,100 458,700 538,700" fill="url(#ray)" opacity="0.5"/>
  </svg>

  <div class="logo" role="img" aria-label="Club logo with cheering crowd silhouettes">
    <div class="logo-name">THE<br>ENCORE</div>
  </div>

  <h1 class="headline">COMING&nbsp; SOON!</h1>
  <p class="tagline">BE PART OF THE NEWEST CHAPTER</p>
  <p class="subline">IN SEATTLE'S LGBT NIGHTLIFE HISTORY</p>

  <div class="crowd" role="img" aria-label="Silhouette of a cheering crowd with raised hands"></div>

  <section class="funding-panel">
    <div class="levels-box">
      <h2 class="levels-title">CROWDFUNDING LEVELS</h2>
      <ul class="levels-col left">
        <li class="level">$25 Opening Fri or Sat night Glitter Hour GA Ticket w/Drag Megastar. <em>(only 100 Available Per Night)</em></li>
        <li class="level">$50 Opening Fri or Sat Night Glitter Hour Third Tier Seating <em>(Only 60 Available Per Night)</em></li>
        <li class="level">$75 Opening Fri or Sat Night Glitter Hour Middle Tier seating Ticket w/secret Drag Megastar. <em>(Only 60 Available Per Night)</em></li>
        <li class="note">*Ask about The Encore Elite Pass</li>
      </ul>
      <div class="divider"></div>
      <ul class="levels-col right">
        <li class="level">$100 Opening Fri or Sat Night Glitter Hour VIP Ticket w/secret Drag Megastar. <em>(Only 60 Available Per Night)</em></li>
        <li class="level">$500 The Encore Pass Skip the line and free cover for 6 months. Not including Brunch Shows and Special Events. Plus The Encore Merch <em>(50 Available)</em></li>
        <li class="level">$1,000 The Encore Gold Pass. Skip the line and free cover for the year. Not including Brunch Shows and Special Events Plus The Encore Merch. <em>(100 Available)</em></li>
      </ul>
    </div>
    <p class="site">WWW.THEENCORENIGHT.COM</p>
  </section>
</main>
</body>
</html>
```